Boutique Barre Studio in Geneva

Business card for pilates and dance studio. We are a brand new studio and love our fresh image with our yellow color. This business card is meant for our founder.

```html
<!DOCTYPE html>
<html lang="en">
<head>
<meta charset="utf-8">
<title>Barre Lune – Founder Business Card</title>
<link rel="stylesheet" href="https://fonts.googleapis.com/css2?family=Montserrat:wght@400;500;600&display=swap">
<style>
  :root {
    --backdrop: #464648;
    --card: #000000;
    --lemon: #f2e482;
    --photo-top: #efe29a;
    --photo-bottom: #d9c97a;
  }
  * { margin: 0; padding: 0; box-sizing: border-box; }
  html, body { width: 1200px; height: 1200px; overflow: hidden; }
  body {
    background: var(--backdrop);
    font-family: "Montserrat", Arial, sans-serif;
    color: var(--lemon);
    position: relative;
  }
  .card {
    position: absolute;
    left: 233px;
    width: 734px;
    height: 447px;
    background: var(--card);
    border-radius: 38px;
    overflow: hidden;
  }
  .card--front { top: 129px; }
  .card--back { top: 623px; }

  .brand-name {
    position: absolute;
    font-weight: 500;
    letter-spacing: 1px;
    white-space: nowrap;
    line-height: 1;
  }
  .card--front .brand-name {
    left: 0; right: 0;
    top: 160px;
    text-align: center;
    font-size: 82px;
  }
  .social-row {
    position: absolute;
    left: 0; right: 0;
    top: 348px;
    display: flex;
    justify-content: center;
    align-items: center;
    gap: 8px;
    font-size: 21px;
    font-weight: 400;
    letter-spacing: 0.5px;
  }
  .social-row .label { margin-right: 6px; }
  .social-dot {
    width: 26px; height: 26px;
    border-radius: 50%;
    background: var(--lemon);
  }

  .card--back .brand-name {
    left: 46px;
    top: 92px;
    font-size: 60px;
  }
  .founder {
    position: absolute;
    left: 47px;
    top: 270px;
  }
  .founder-name { font-size: 25px; font-weight: 600; line-height: 1.1; }
  .founder-role { font-size: 16px; font-weight: 400; margin-top: 2px; }
  .contact-list {
    position: absolute;
    left: 46px;
    top: 333px;
    list-style: none;
  }
  .contact-list li {
    display: flex;
    align-items: center;
    gap: 9px;
    font-size: 17px;
    height: 22.5px;
  }
  .contact-list svg { width: 20px; height: 20px; flex: none; }

  .studio-photo {
    position: absolute;
    left: 353px;
    top: 76px;
    width: 340px;
    height: 340px;
    border-radius: 50%;
    background: radial-gradient(circle at 45% 40%, var(--photo-top), var(--photo-bottom));
  }
</style>
</head>
<body>
  <section class="card card--front">
    <div class="brand-name">barre lune</div>
    <div class="social-row">
      <span class="label">Find on us:</span>
      <span class="social-dot"></span>
      <span class="social-dot"></span>
      <span class="social-dot"></span>
    </div>
  </section>

  <section class="card card--back">
    <div class="brand-name">barre lune</div>

    <div class="founder">
      <div class="founder-name">Lena Moravec</div>
      <div class="founder-role">Owner</div>
    </div>

    <ul class="contact-list">
      <li>
        <svg viewBox="0 0 24 24" fill="currentColor"><path d="M6.6 10.8c1.4 2.8 3.8 5.1 6.6 6.6l2.2-2.2c.3-.3.7-.4 1-.2 1.1.4 2.3.6 3.6.6.6 0 1 .4 1 1V20c0 .6-.4 1-1 1C10.6 21 3 13.4 3 4c0-.6.4-1 1-1h3.5c.6 0 1 .4 1 1 0 1.3.2 2.5.6 3.6.1.3 0 .7-.2 1l-2.3 2.2z"/></svg>
        <span>022-555-0148</span>
      </li>
      <li>
        <svg viewBox="0 0 24 24" fill="currentColor"><path d="M2 5h20v14H2z M4 7v.4l8 5.6 8-5.6V7z" fill-rule="evenodd"/></svg>
        <span>lmoravec@barrelune.com</span>
      </li>
      <li>
        <svg viewBox="0 0 24 24" fill="none" stroke="currentColor" stroke-width="1.8"><circle cx="12" cy="12" r="9"/><ellipse cx="12" cy="12" rx="4" ry="9"/><path d="M3 12h18M5 7h14M5 17h14"/></svg>
        <span>barrelune.com</span>
      </li>
    </ul>

    <div class="studio-photo" role="img" aria-label="Photo of students practising aerial yoga in hammocks, tinted yellow"></div>
  </section>
</body>
</html>
```